Brochure Design Project

Our company is KMV Sable Ridge. (no LOGO)

We are a restaurant marketing and advertising service. We market restaurants menus by producing a menu guide, distributing flyers and post cards, and also placing the restaurants menu on our website for delivery.

We make restaurants more profitable, by making their food more accessible. Marketing restaurants on search engines, websites, plazanet, wunq, zintro, and a total of 21 different marketing techniques that make restaurants more money.

Key Point: This is all done at NO COST to the restaurant.

We are looking for a design for a brochure that will be mailed as well as handed to restaurateurs.

In my attached file I am including our sales letter. The letter can stay in letter form for the inside of a tri-fold brochure or it can be part of your design.

For more information about our service, please read the attached sales letter.
Updates

Target Market(s)

Restaurant Owners and General managers

Industry/Entity Type

Advertising

Requirements
Must have
• Must look attractive and Eye-catching

```html
<!DOCTYPE html>
<html lang="en">
<head>
<meta charset="utf-8">
<title>KMV Sable Ridge – Restaurant Marketing Flyer</title>
<link href="https://fonts.googleapis.com/css2?family=Archivo+Black&family=Oswald:wght@500;600&family=PT+Sans+Narrow:wght@400;700&family=Cabin:wght@500&display=swap" rel="stylesheet">
<style>
  :root {
    --red: #b3161c;
    --ink: #1a1a1a;
    --grey-text: #3a3a3a;
    --page: #ffffff;
    --panel-light: #f4f4f4;
    --panel-mid: #c9cacc;
    --suit: #17181b;
    --footer-strip: #b9bcc0;
  }
  * { margin: 0; padding: 0; box-sizing: border-box; }
  html, body { width: 1200px; height: 900px; overflow: hidden; background: var(--page); }
  .canvas { position: relative; width: 1200px; height: 900px; }

  .flyer {
    position: absolute; left: 301px; top: 25px; width: 599px; height: 850px;
    background: var(--page); overflow: hidden;
  }
  .top-band {
    position: absolute; left: 0; top: 0; width: 100%; height: 32px;
    background: var(--red); color: #fff;
    font: 700 11.5px/32px "PT Sans Narrow", sans-serif;
    text-align: center; letter-spacing: 0.1px;
  }
  .hero {
    position: absolute; left: 0; top: 32px; width: 100%; height: 498px;
    background: radial-gradient(ellipse at 45% 25%, var(--panel-light) 0%, #e4e4e5 45%, var(--panel-mid) 100%);
  }
  .hero-photo {
    position: absolute; left: 240px; top: 0; width: 359px; height: 498px;
    background: linear-gradient(90deg, rgba(23,24,27,0) 0%, rgba(23,24,27,0.15) 30%, rgba(23,24,27,0.85) 62%, var(--suit) 80%);
  }
  .headline {
    position: absolute; left: 110px; top: 68px; width: 340px;
    font: 400 38px/0.82 "Archivo Black", sans-serif;
    color: #000; text-align: center; letter-spacing: -1.5px; text-transform: uppercase;
  }
  .hero-copy {
    position: absolute; left: 37px; top: 258px; width: 285px;
    font: 400 10.4px/13px "PT Sans Narrow", sans-serif; color: var(--ink);
  }
  .hero-copy p + p { margin-top: 13px; }

  .guarantee {
    position: absolute; left: 38px; top: 555px; width: 170px;
    font-family: "Oswald", sans-serif; text-align: center;
  }
  .guarantee .big {
    display: block; color: var(--red); font-weight: 600; letter-spacing: -6px;
  }
  .guarantee .we { font-size: 140px; line-height: 120px; margin-top: 0; }
  .guarantee .word {
    display: block; color: var(--ink); font-weight: 500; font-size: 27px; line-height: 24px;
    letter-spacing: -0.5px; margin-left: -2px;
  }
  .guarantee .it { font-size: 178px; line-height: 150px; }

  .letter {
    position: absolute; left: 230px; top: 560px; width: 320px;
    font: 400 10.4px/13px "PT Sans Narrow", sans-serif; color: var(--ink);
    text-align: justify;
  }
  .letter p + p { margin-top: 8px; }
  .letter strong { font-weight: 700; }
  .letter .no-cost { color: var(--red); font-weight: 700; font-size: 12px; }
  .letter .ps { text-align: left; }

  .signoff {
    position: absolute; left: 230px; top: 762px; width: 322px;
    border-top: 2px solid var(--ink);
    font: 500 41px/1 "Cabin", sans-serif; color: var(--grey-text);
    padding-top: 6px; letter-spacing: -0.5px;
  }
  .foot-strip {
    position: absolute; left: 0; bottom: 0; width: 100%; height: 7px; background: var(--footer-strip);
  }
</style>
</head>
<body>
<div class="canvas">
  <article class="flyer">
    <div class="top-band">WOULD A CHECK FOR $18,375 WITH YOUR RESTAURANTS NAME ON IT BE WORTH A 15 MIN CONVERSATION?</div>

    <section class="hero">
      <div class="hero-photo" role="img" aria-label="Waiter in a black suit and white glove holding a silver tray, with a white towel over his arm"></div>
      <h1 class="headline">Are you tired of ineffective marketing and advertising?</h1>
      <div class="hero-copy">
        <p>If you answered yes to either question, we should talk about our all-inclusive marketing plan. Our marketing plan places your menu in front of thousands of customers each and every month. Hungry customers looking to buy immediately. Hungry customers that want food now. The more views your menu receives, the more likely a customer will purchase food from your restaurant.</p>
        <p>Ever have a problem with down time at your restaurant? Customers are not dining in or taking out because it's too hot or too cold or it's raining outside? That's a problem that you wouldn't have to have, if you made your food more accessible.</p>
        <p>KMV Sable Ridge is a full service restaurant marketing and advertising service that specializes in delivery. We deliver food from a variety of restaurants to people at their homes, offices, and hotels! Using our marketing plan we will bring more exposure to your restaurant and increase your bottom line.</p>
      </div>
    </section>

    <div class="guarantee" aria-label="We guarantee it!">
      <span class="big we">WE</span>
      <span class="word">GUARANTEE</span>
      <span class="big it">IT!</span>
    </div>

    <div class="letter">
      <p><strong>How many marketers and advertisers say that?</strong><br>
      We do! We guarantee that you will only make money and not pay money. There are never any participation cost, or fees associated with our service. We use a combination of 21 proven Marketing techniques to drive your profits up while keeping cost down.</p>
      <p>So what should you do? Call me nowat 555-014-2286 to schedule a 15 min consultation that is guaranteed to <span class="no-cost">NOT COST</span> you anything and only make your restaurant money.</p>
      <p>Talk to you soon!</p>
      <p class="ps"><strong>Ross Whitley - 555-014-2286 (cell) - kmvsableridge.com</strong><br>
      p.s.<br>
      I have a check with your restaurants name on it, so contact me before July 26, 2013!<br>
      You can also schedule an appointment online at kmvsableridge.com</p>
    </div>

    <div class="signoff">KMV Sable Ridge</div>
    <div class="foot-strip"></div>
  </article>
</div>
</body>
</html>
```